Brochure Cover and Back pages

We are a US-based cosmetics company that sells state-of-the-art skin care products, including advanced anti-aging serums, natural mineral sunscreens, organic antioxidant moisturizers, and organic face cleansers. We need a product brochure. We already have chosen a design for the layout of the product info pages. But we still need a cover page and a back page. We are looking for simple but elegant design for the cover page. The back page is less important and we already know what we want on the back page. It will be the company's mission statement and at the bottom, the company URL, phone number, etc.

The brochure has two folds. So there will be three panels on both sides. The size of each panel is 16.5 (l) x 9.5 (w) cm.

At the end of the project, we expect the designer to integrate all the pages so that the finished copy is read to be sent off to a printing service for printing.

All the product info pages are attached. Also attached are the text (info) to go on the back page, company logo with and without the tagline, the icon in the logo.

YOu are welcome to visit our website www.morvask.com to learn about our products.

Industry/Entity Type

Cosmetics

```html
<!DOCTYPE html>
<html lang="en">
<head>
<meta charset="utf-8">
<title>Morvask Brochure – Cover and Back Panels</title>
<link rel="stylesheet" href="https://fonts.googleapis.com/css2?family=Arimo:wght@400;700&family=Fondamento&display=swap">
<style>
  :root {
    --page-bg: #e6e2de;
    --sheet: #f2f2f2;
    --sheet-left: #efeeee;
    --plum: #5f4650;
    --heading: #5a4652;
    --body-text: #2e2e2e;
    --rose: #ea1c4f;
    --blush: #f7c6c4;
    --divider: #3a3a3a;
    --ink: #1c1c1c;
  }
  * { margin: 0; padding: 0; box-sizing: border-box; }
  html, body { width: 1200px; height: 719px; overflow: hidden; }
  body { background: var(--page-bg); font-family: "Arimo", Arial, sans-serif; position: relative; }

  .brochure {
    position: absolute; left: 52px; top: 38px;
    width: 1096px; height: 634px;
    background: var(--sheet);
    overflow: hidden;
    box-shadow: 0 2px 8px rgba(0,0,0,0.18);
  }
  .panel { position: absolute; top: 0; height: 634px; }
  .panel--about { left: 0; width: 366px; background: var(--sheet-left); }
  .panel--contact { left: 366px; width: 364px; }
  .panel--cover { left: 730px; width: 366px; }

  .fold { position: absolute; top: 0; width: 1px; height: 634px; background: var(--divider); z-index: 3; }
  .fold--first { left: 366px; }
  .fold--second { left: 730px; }

  .artwork { position: absolute; inset: 0; z-index: 1; }

  /* About panel */
  .about { position: absolute; left: 20px; top: 22px; width: 318px; color: var(--body-text); z-index: 2; }
  .about__title { font-size: 16px; font-weight: 400; color: var(--heading); text-decoration: underline; }
  .about__subtitle { margin-top: 23px; font-size: 16.5px; font-weight: 400; color: var(--heading); }
  .about__intro { margin-top: 9px; font-size: 13.4px; line-height: 19.6px; text-align: justify; }
  .about__mission { margin-top: 26px; font-size: 17px; font-weight: 400; color: var(--heading); }
  .mission-list { list-style: none; margin-top: 6px; padding-left: 2px; font-size: 13.4px; line-height: 19.6px; }
  .mission-list li::before { content: "•"; margin-right: 4px; }
  .about__body { margin-top: 16px; padding-left: 3px; width: 307px; font-size: 13.4px; line-height: 19.5px; text-align: justify; }

  /* Contact panel */
  .contact-brand { position: absolute; left: 0; width: 364px; top: 312px; text-align: center; z-index: 2;
    font-size: 30px; font-weight: 700; color: var(--blush); }
  .contact-brand__dot { display: block; width: 18px; height: 18px; border-radius: 50%; background: var(--blush); margin: 0 auto 10px; }
  .contact { position: absolute; left: 0; width: 364px; top: 462px; text-align: center; color: var(--ink);
    font-size: 14.6px; line-height: 16.5px; letter-spacing: 0.3px; z-index: 2; }
  .contact__block + .contact__block { margin-top: 6px; }
  .contact__icon { display: inline-block; vertical-align: -2px; margin-right: 5px; }
  .contact__web { font-size: 13.6px; }

  /* Cover panel */
  .tagline { position: absolute; right: 16px; top: 406px; text-align: right; z-index: 2;
    font-family: "Fondamento", Georgia, serif; color: var(--ink); font-size: 30px; line-height: 50px; }
  .wordmark { position: absolute; right: 16px; top: 550px; z-index: 2;
    font-family: "Arimo", Arial, sans-serif; font-weight: 700; font-size: 58px; line-height: 60px; color: var(--ink); letter-spacing: -1px; }
</style>
</head>
<body>
<main class="brochure">
  <section class="panel panel--about">
    <div class="about">
      <h2 class="about__title">About Us</h2>
      <h3 class="about__subtitle">Who We Are</h3>
      <p class="about__intro">Morvask is a cosmetics company dedicated to developing high quality and high performance skin care products. Morvask’s science-based approach promises to deliver smart skin care to consumers!</p>
      <h3 class="about__mission">Our Mission:</h3>
      <ul class="mission-list">
        <li>To Create Beauty Solutions through Science</li>
        <li>To Inform and Empower Consumers</li>
        <li>To Create Beauty Solutions through Science</li>
      </ul>
      <p class="about__body">Skin is one of the most, if not the most,researched organs in the human body.As a result, tremendous progress has been made over the past few decades in our understanding of the skin, its functions and various physiological processes. As science advances, we will surely learn even more about the skin and how to keep it healthy and delay its aging. For now, what science has already learned about skin care is what drives our product development work. We have made it our mission to create useful and effective skin care and beauty products based on the findings of clinical studies and scientific research.</p>
    </div>
  </section>

  <section class="panel panel--contact">
    <div class="contact-brand"><span class="contact-brand__dot"></span>Morvask</div>
    <address class="contact" style="font-style: normal;">
      <div class="contact__block">
        <svg class="contact__icon" width="11" height="15" viewBox="0 0 11 15" aria-hidden="true"><path d="M5.5 0C2.5 0 0 2.4 0 5.4 0 9.4 5.5 15 5.5 15S11 9.4 11 5.4C11 2.4 8.5 0 5.5 0Zm0 7.6a2.2 2.2 0 1 1 0-4.4 2.2 2.2 0 0 1 0 4.4Z" fill="#1c1c1c"/></svg>2190 Larkspur Ave. Ste. 400<br>Walnut Grove, CA 94590<br>USA
      </div>
      <div class="contact__block">
        <svg class="contact__icon" width="14" height="14" viewBox="0 0 14 14" aria-hidden="true"><circle cx="7" cy="7" r="6.3" fill="none" stroke="#1c1c1c" stroke-width="1.2"/><path d="M5 3.6 6.2 5.4 5.5 6.3C6 7.4 6.7 8.1 7.8 8.6L8.7 7.9 10.4 9.1 9.6 10.4C7 10.2 3.9 7.1 3.7 4.5Z" fill="#1c1c1c"/></svg>(1-855-555-0142)<br>1-866-555-0187<br>(925) 555-0163
      </div>
      <div class="contact__block contact__web">
        <svg class="contact__icon" width="13" height="13" viewBox="0 0 13 13" aria-hidden="true"><g fill="none" stroke="#1c1c1c" stroke-width="1"><circle cx="6.5" cy="6.5" r="6"/><ellipse cx="6.5" cy="6.5" rx="2.6" ry="6"/><path d="M0.5 6.5h12M1.5 3.5h10M1.5 9.5h10"/></g></svg>www.Morvask.com
      </div>
    </address>
  </section>

  <svg class="artwork" width="1096" height="634" viewBox="0 0 1096 634" aria-hidden="false">
    <defs>
      <linearGradient id="portrait-tone" x1="0" y1="0" x2="1" y2="0">
        <stop offset="0" stop-color="#efe4de"/>
        <stop offset="0.35" stop-color="#e6c4b3"/>
        <stop offset="0.7" stop-color="#dcb19d"/>
        <stop offset="0.82" stop-color="#2f5a2a"/>
        <stop offset="1" stop-color="#1d3f1a"/>
      </linearGradient>
    </defs>
    <path class="swoosh" fill="#5f4650"
      d="M700,0 L730,0 C748,110 768,200 792,250 C835,340 882,432 862,522 C846,592 785,624 730,634 L476,634 C620,612 760,562 800,482 C840,402 722,262 716,162 C712,100 706,50 700,0 Z"/>
    <path class="swoosh-line" fill="none" stroke="#5f4650" stroke-width="3"
      d="M808,262 C790,300 800,340 830,372"/>
    <path role="img" aria-label="Photograph: woman's face with a glossy green leaf covering one eye"
      fill="url(#portrait-tone)"
      d="M772,0 L1096,0 L1096,250 C1000,318 884,318 812,262 C792,220 782,120 772,0 Z"/>
    <path class="accent-band" fill="#ea1c4f"
      d="M806,256 C850,326 968,340 1096,252 L1096,394 C992,392 866,372 826,332 C808,312 802,282 806,256 Z"/>
    <path fill="#f2f2f2"
      d="M830,318 C890,350 990,348 1096,292 L1096,300 C990,360 890,362 830,318 Z"/>
  </svg>

  <div class="fold fold--first"></div>
  <div class="fold fold--second"></div>

  <section class="panel panel--cover" style="z-index:2;">
    <p class="tagline">Bringing You<br>Smart Skin Care</p>
    <h1 class="wordmark">Morvask</h1>
  </section>
</main>
</body>
</html>
```